Business card design and logo needed - Photographer

I take photos of weddings, rodeos, snowmobiling.
Need a card to hand out to prospective clients.
Industry/Entity Type
Business
Contact Information for Business Card
Marcus Dolven Photography
Requirements
Must have
- Bold
Black or white base.
My website. www.MarcusDolven.example
Should not have
- camera/ lens/ aperture blades

```html
<!DOCTYPE html>
<html lang="en">
<head>
<meta charset="utf-8">
<title>Marcus Dolven Photography – Business Card</title>
<link rel="stylesheet" href="https://fonts.googleapis.com/css2?family=Questrial&display=swap">
<style>
  :root {
    --page-bg: #2a2a2a;
    --card-dark: #050505;
    --card-mid: #1a1a1a;
    --text-silver: #c9c9c9;
    --text-grey: #a8a8a8;
    --divider: #000000;
    --divider-light: #2c2c2c;
    --photo-green-a: #7f9e45;
    --photo-green-b: #6a8a36;
    --photo-grey-a: #8a8f80;
    --photo-grey-b: #a9ad9f;
    --photo-sea-a: #b9d8df;
    --photo-sea-b: #8fc2cf;
  }
  * { margin: 0; padding: 0; box-sizing: border-box; }
  html, body {
    width: 1200px;
    height: 1000px;
    overflow: hidden;
    background: var(--page-bg);
  }
  .business-card {
    position: absolute;
    left: 76px;
    top: 200px;
    width: 1048px;
    height: 600px;
    background:
      radial-gradient(ellipse 520px 380px at 420px 300px, var(--card-mid) 0%, var(--card-dark) 100%);
    box-shadow: 0 6px 18px rgba(0, 0, 0, 0.5);
    font-family: "Questrial", sans-serif;
  }
  .brand {
    position: absolute;
    right: 663px;
    top: 270px;
    text-align: right;
    white-space: nowrap;
  }
  .brand-name {
    font-size: 38px;
    letter-spacing: 1px;
    line-height: 1;
    color: var(--text-silver);
    text-transform: uppercase;
    font-weight: 400;
  }
  .brand-tagline {
    margin-top: 6px;
    font-size: 17px;
    letter-spacing: 1.5px;
    color: var(--text-grey);
    text-transform: uppercase;
  }
  .divider {
    position: absolute;
    left: 414px;
    top: 215px;
    width: 3px;
    height: 200px;
    background: linear-gradient(to bottom, transparent, var(--divider) 30%, var(--divider) 70%, transparent);
    border-right: 1px solid var(--divider-light);
    opacity: 0.9;
  }
  .photo {
    position: absolute;
  }
  .photo-portrait {
    left: 435px; top: 85px; width: 277px; height: 185px;
    background: linear-gradient(135deg, var(--photo-green-a), var(--photo-green-b));
  }
  .photo-couple {
    left: 730px; top: 83px; width: 279px; height: 187px;
    background: linear-gradient(135deg, var(--photo-grey-a), var(--photo-grey-b));
  }
  .photo-sailing {
    left: 526px; top: 314px; width: 388px; height: 214px;
    background: linear-gradient(160deg, var(--photo-sea-a), var(--photo-sea-b));
  }
  .website {
    position: absolute;
    left: 48px;
    top: 532px;
    font-size: 17px;
    letter-spacing: 2px;
    color: var(--text-silver);
    text-transform: uppercase;
    white-space: nowrap;
  }
</style>
</head>
<body>
  <main class="business-card">
    <div class="brand">
      <div class="brand-name">Marcus Dolven</div>
      <div class="brand-tagline">Photography</div>
    </div>
    <div class="divider"></div>
    <div class="photo photo-portrait" role="img" aria-label="Photo of a smiling bride on a green lawn"></div>
    <div class="photo photo-couple" role="img" aria-label="Photo of a wedding couple's hands forming a heart"></div>
    <div class="photo photo-sailing" role="img" aria-label="Photo of a woman steering a sailboat at sea"></div>
    <div class="website">www.MarcusDolven.example</div>
  </main>
</body>
</html>
```